Deactivated Coal-Fired Power Plant to be redeveloped into a Green Energy Campus.

Want a striking business card statement that introduces our concept project to provide economic and community recovery to a former rural coal community in western PA.
Essentially 12 project representatives that will lead both the demolition of an existing power plant and the redevelopment to a new Green energy site.
Business Card should reflect our effort.
We are open to ideas.

Target Market(s)

Energy and Power Generation industries

Industry/Entity Type

Power Generation and Data Centers

Contact Information for Business Card

Included in uploaded materials

Font styles to use
Sans Serif
Other font styles liked:
• Arial, Calibri

Requirements
Must have
• Multiple colors

```html
<!DOCTYPE html>
<html lang="en">
<head>
<meta charset="utf-8">
<title>Ridgeline Renewal – Business Card</title>
<link rel="stylesheet" href="https://fonts.googleapis.com/css2?family=Arimo:ital,wght@0,400;0,700;1,400;1,700&family=Montserrat:wght@700&display=swap">
<style>
  :root {
    --green: #16924a;
    --green-dark: #0f7a3c;
    --black: #050505;
    --white: #f4f5f4;
    --page: #e6e7e6;
    --text-light: #ffffff;
  }
  * { box-sizing: border-box; margin: 0; padding: 0; }
  html, body {
    width: 1200px; height: 768px; overflow: hidden;
    background: var(--page);
    font-family: "Arimo", Arial, sans-serif;
  }
  .sheet {
    width: 1200px; height: 768px;
    display: flex; align-items: center; justify-content: center; gap: 40px;
  }
  .card {
    position: relative;
    width: 540px; height: 309px;
    border-radius: 22px;
    overflow: hidden;
    box-shadow: 0 6px 18px rgba(0,0,0,.18);
  }

  /* Back side */
  .card-back { background: var(--green); }
  .card-back .brand {
    position: absolute; left: 0; right: 0; top: 96px;
    display: flex; align-items: center; justify-content: center; gap: 16px;
  }
  .card-back .brand-dot {
    width: 46px; height: 46px; border-radius: 50%;
    background: var(--white);
  }
  .card-back .brand-name {
    font-family: "Arimo", Arial, sans-serif;
    font-weight: 700; font-size: 34px; letter-spacing: 1px;
    color: var(--text-light); text-transform: uppercase;
  }
  .card-back .baseline {
    position: absolute; left: 120px; right: 120px; top: 172px;
    height: 2px; background: var(--black);
  }
  .card-back .tagline {
    position: absolute; left: 0; right: 0; top: 196px;
    text-align: center; color: var(--text-light);
    font-size: 13px; letter-spacing: 4px;
  }

  /* Front side */
  .card-front { background: var(--black); }
  .card-front .curve { position: absolute; inset: 0; }
  .card-front .person {
    position: absolute; left: 34px; top: 30px;
  }
  .card-front .person-name {
    color: var(--green); font-weight: 700; font-style: italic;
    font-size: 22px;
  }
  .card-front .person-title {
    color: var(--text-light); font-style: italic; font-size: 13px; margin-top: 2px;
  }
  .card-front .company {
    position: absolute; left: 34px; top: 156px;
    color: var(--text-light); font-size: 14px;
  }
  .card-front .contacts {
    position: absolute; left: 34px; top: 186px;
    list-style: none; color: var(--text-light); font-size: 13.5px;
  }
  .card-front .contacts li {
    display: flex; align-items: center; gap: 8px; height: 21px;
  }
  .card-front .contacts svg { width: 12px; height: 12px; fill: var(--green); flex: none; }
  .card-front .brand {
    position: absolute; left: 378px; top: 112px; width: 150px;
    display: flex; flex-direction: column; align-items: center; gap: 8px;
  }
  .card-front .brand-dot {
    width: 40px; height: 40px; border-radius: 50%; background: var(--green);
  }
  .card-front .brand-name {
    font-weight: 700; font-size: 19px; color: var(--black);
    text-transform: uppercase; text-align: center; line-height: 1.1;
  }
</style>
</head>
<body>
<main class="sheet">

  <section class="card card-back" aria-label="Card back">
    <div class="brand">
      <span class="brand-dot"></span>
      <span class="brand-name">Ridgeline Renewal</span>
    </div>
    <div class="baseline"></div>
    <p class="tagline">Your energy future</p>
  </section>

  <section class="card card-front" aria-label="Card front">
    <svg class="curve" viewBox="0 0 540 309" preserveAspectRatio="none" aria-hidden="true">
      <path d="M420 0 C345 40 328 200 372 309 L540 309 L540 0 Z" fill="var(--green)"/>
      <path d="M428 0 C358 44 342 200 384 309 L540 309 L540 0 Z" fill="var(--white)"/>
    </svg>

    <div class="person">
      <p class="person-name">Daniel Whitcombe</p>
      <p class="person-title">Chief Operation Officer</p>
    </div>

    <p class="company">Ridgeline Renewal Partners LLC</p>

    <ul class="contacts">
      <li>
        <svg viewBox="0 0 24 24"><path d="M6.6 10.8a15.1 15.1 0 0 0 6.6 6.6l2.2-2.2a1 1 0 0 1 1-.25 11.4 11.4 0 0 0 3.6.57 1 1 0 0 1 1 1V20a1 1 0 0 1-1 1A17 17 0 0 1 3 4a1 1 0 0 1 1-1h3.5a1 1 0 0 1 1 1c0 1.25.2 2.45.57 3.57a1 1 0 0 1-.25 1z"/></svg>
        555.214.7380
      </li>
      <li>
        <svg viewBox="0 0 24 24"><path d="M2 5h20v14H2z" opacity=".0"/><path d="M2 5h20v2l-10 6L2 7zm0 4l10 6 10-6v10H2z"/></svg>
        dwhitcombe@ridgelinerenewal.com
      </li>
      <li>
        <svg viewBox="0 0 24 24"><circle cx="12" cy="12" r="10"/></svg>
        www.ridgelinerenewal.com
      </li>
    </ul>

    <div class="brand">
      <span class="brand-dot"></span>
      <span class="brand-name">Ridgeline Renewal</span>
    </div>
  </section>

</main>
</body>
</html>
```